BrightMesa Business Card Contest

We are looking for a modern business card that catches attention and is unique. Attached is the brand guide and logo files. Please note that the back side (not the side with our name and info) with be UV raise printed, so have fun with the design there. We want to include Name, Title, Phone number, email, website.

Contact Information for Business Card

Please see project description

```html
<!DOCTYPE html>
<html lang="en">
<head>
<meta charset="utf-8">
<title>BrightMesa Business Card</title>
<link rel="stylesheet" href="https://fonts.googleapis.com/css2?family=Montserrat:wght@400;700&family=Outfit:wght@300;400;500&display=swap">
<style>
  :root {
    --page: #ececee;
    --card: #1f2026;
    --white: #ffffff;
    --muted: #d6d7da;
    --accent-blue: #1e63c6;
    --accent-cyan: #22bfe6;
    --accent-sage: #9aa57c;
    --accent-orange: #f08a24;
    --accent-red: #e0322a;
    --title-cyan: #27b8e3;
  }
  * { box-sizing: border-box; margin: 0; padding: 0; }
  html, body { width: 1156px; height: 1200px; overflow: hidden; }
  body {
    background: var(--page);
    display: flex;
    flex-direction: column;
    align-items: center;
    justify-content: center;
    gap: 34px;
    font-family: "Outfit", sans-serif;
  }
  .card {
    position: relative;
    width: 960px;
    height: 550px;
    background: var(--card);
    box-shadow: 0 6px 18px rgba(0,0,0,0.25);
    overflow: hidden;
  }
  .spectrum-line {
    position: absolute;
    left: 0;
    width: 100%;
    height: 9px;
    background: linear-gradient(90deg, var(--accent-blue) 0%, var(--accent-cyan) 25%, var(--accent-sage) 50%, var(--accent-orange) 75%, var(--accent-red) 100%);
  }

  /* Back side */
  .card-back .brand-wordmark {
    position: absolute;
    left: 56px;
    top: 150px;
    font-family: "Outfit", sans-serif;
    font-weight: 500;
    font-size: 96px;
    letter-spacing: -1px;
    color: var(--accent-orange);
  }
  .card-back .brand-block {
    position: absolute;
    left: 648px;
    top: 56px;
    width: 236px;
    height: 236px;
    background: var(--accent-cyan);
  }
  .card-back .spectrum-line { top: 470px; }

  /* Front side */
  .holder {
    position: absolute;
    left: 56px;
    top: 58px;
    font-family: "Montserrat", sans-serif;
    color: var(--white);
  }
  .holder-first {
    font-weight: 700;
    font-size: 54px;
    line-height: 1;
    letter-spacing: 0.5px;
  }
  .holder-last {
    font-weight: 400;
    font-size: 48px;
    line-height: 1.05;
    letter-spacing: 0.5px;
  }
  .holder-title {
    margin-top: 12px;
    font-family: "Outfit", sans-serif;
    font-weight: 500;
    font-size: 16px;
    letter-spacing: 0.3px;
    color: var(--title-cyan);
  }
  .card-front .spectrum-line { top: 270px; }
  .company {
    position: absolute;
    left: 56px;
    top: 408px;
    display: flex;
    align-items: center;
    gap: 16px;
  }
  .company-mark {
    width: 62px;
    height: 62px;
    background: var(--accent-cyan);
  }
  .company-name {
    font-family: "Outfit", sans-serif;
    font-weight: 400;
    font-size: 68px;
    color: var(--white);
    letter-spacing: -0.5px;
    line-height: 1;
  }
  .contact-list {
    position: absolute;
    right: 42px;
    top: 380px;
    list-style: none;
    display: flex;
    flex-direction: column;
    gap: 20px;
  }
  .contact-item {
    display: flex;
    align-items: center;
    justify-content: flex-end;
    gap: 18px;
    font-size: 19px;
    font-weight: 300;
    color: var(--muted);
  }
  .contact-icon { width: 26px; height: 26px; flex: none; }
</style>
</head>
<body>

  <section class="card card-back" aria-label="Card back">
    <div class="brand-wordmark">BrightMesa</div>
    <div class="brand-block" aria-hidden="true"></div>
    <div class="spectrum-line"></div>
  </section>

  <section class="card card-front" aria-label="Card front">
    <div class="holder">
      <div class="holder-first">JORDAN</div>
      <div class="holder-last">REYES</div>
      <div class="holder-title">MANAGING DIRECTOR</div>
    </div>
    <div class="spectrum-line"></div>

    <div class="company">
      <div class="company-mark" aria-hidden="true"></div>
      <div class="company-name">BrightMesa</div>
    </div>

    <ul class="contact-list">
      <li class="contact-item">
        <span>+960 555 0142</span>
        <svg class="contact-icon" viewBox="0 0 24 24" aria-hidden="true">
          <path fill="#d6d7da" d="M6.6 10.8a15.1 15.1 0 0 0 6.6 6.6l2.2-2.2a1 1 0 0 1 1-.25 11.4 11.4 0 0 0 3.6.57 1 1 0 0 1 1 1V20a1 1 0 0 1-1 1A17 17 0 0 1 3 4a1 1 0 0 1 1-1h3.5a1 1 0 0 1 1 1c0 1.25.2 2.45.57 3.57a1 1 0 0 1-.25 1z"/>
        </svg>
      </li>
      <li class="contact-item">
        <span>jordan@brightmesa.com</span>
        <svg class="contact-icon" viewBox="0 0 24 24" aria-hidden="true">
          <rect x="2" y="4" width="20" height="16" rx="1.5" fill="#d6d7da"/>
          <path d="M3 6l9 7 9-7" fill="none" stroke="#1f2026" stroke-width="2"/>
        </svg>
      </li>
      <li class="contact-item">
        <span>www.brightmesa.com</span>
        <svg class="contact-icon" viewBox="0 0 24 24" aria-hidden="true">
          <g fill="none" stroke="#d6d7da" stroke-width="1.8">
            <circle cx="12" cy="12" r="10"/>
            <ellipse cx="12" cy="12" rx="4.5" ry="10"/>
            <line x1="2" y1="12" x2="22" y2="12"/>
            <line x1="12" y1="2" x2="12" y2="22"/>
          </g>
        </svg>
      </li>
    </ul>
  </section>

</body>
</html>
```